Real Estate Marketing Flyer (To Be Mailed)

Design a Flyer To be Mailed to Potential Home Sellers.
Possible Texts to Use:
*Lehighton Home Owners: Opportunity is Knocking in 2020!
*Industry is moving in
*Housing Inventory is Critically Low
*Entry Level Homes in High Demand
*Qualified Buyers are searching Now
*Interest Rates Projected to Rise by year end
*Now is the Time to Sell
*Trust My Proven Track Record to get the job done well
-----------------------------------------------
My Info for the Piece:
Odile Brankett
Hearthway Realty Partners
2715 Pellow Rd
Whitehall Pa 18094
484 927 3160
610 718 2295
Please use Hearthway Colors of Blue and Red if Possible. Also, I will upload my headshot to use.

```html
<!DOCTYPE html>
<html lang="en">
<head>
<meta charset="utf-8">
<title>Lehighton Opportunity Flyer</title>
<link href="https://fonts.googleapis.com/css2?family=Raleway:wght@300;400;600;700&family=Poppins:wght@300;400&family=Lato:wght@400;700;900&display=swap" rel="stylesheet">
<style>
  :root {
    --backdrop: #d8d7d6;
    --paper: #f7f7f7;
    --brand-red: #e5333b;
    --banner-red: rgba(232, 62, 70, 0.9);
    --ink: #1d1d1f;
    --body-ink: #3a3a3c;
    --footer-dark: #3b3b3f;
    --footer-mid: #5a5a5f;
    --muted: #555559;
  }
  * { margin: 0; padding: 0; box-sizing: border-box; }
  html, body {
    width: 1200px; height: 800px; overflow: hidden;
    background: var(--backdrop);
  }
  .flyer {
    position: absolute; left: 338px; top: 30px;
    width: 523px; height: 740px;
    background: var(--paper);
    overflow: hidden;
    box-shadow: 0 10px 30px rgba(0,0,0,0.18);
    font-family: 'Poppins', sans-serif;
  }
  .hero-photo {
    position: absolute; left: 0; top: 0; width: 523px; height: 279px;
    background: linear-gradient(160deg, #5c7a49 0%, #7a8088 35%, #c9953f 60%, #6f7378 80%, #4f7a3a 100%);
  }
  .headline-panel {
    position: absolute; left: 0; top: 150px; width: 328px; height: 149px;
    background: var(--banner-red);
    border-radius: 0 12px 12px 0;
    box-shadow: 0 -4px 0 4px rgba(255,255,255,0.35);
    font-family: 'Raleway', sans-serif;
    padding-left: 30px;
  }
  .headline-city { position: absolute; left: 30px; top: 12px; font-size: 34px; font-weight: 300; color: #fff; }
  .headline-main { position: absolute; left: 30px; top: 56px; font-size: 34px; font-weight: 700; color: #fff; letter-spacing: 0.5px; }
  .headline-tail { position: absolute; left: 30px; top: 100px; font-size: 31px; font-weight: 400; color: var(--ink); }
  .market-points {
    position: absolute; left: 30px; top: 320px; list-style: none;
  }
  .market-points li {
    position: relative; padding-left: 14px;
    font-size: 17px; font-weight: 300; color: var(--ink);
    height: 33px; line-height: 24px;
  }
  .market-points li::before {
    content: ""; position: absolute; left: 0; top: 8px;
    width: 9px; height: 9px; border-radius: 50%; background: var(--brand-red);
  }
  .call-to-action {
    position: absolute; left: 360px; top: 354px; width: 150px;
    text-align: center; font-family: 'Lato', sans-serif; font-weight: 900;
    font-size: 26px; line-height: 27px; color: var(--brand-red);
  }
  .agent-bio {
    position: absolute; left: 30px; top: 524px; width: 320px;
    font-family: 'Raleway', sans-serif; font-size: 11.5px; font-weight: 400;
    color: var(--body-ink); line-height: 20px;
  }
  .agent-bio p + p { margin-top: 20px; }
  .agent-headshot {
    position: absolute; left: 368px; top: 484px; width: 128px; height: 190px;
    border-radius: 12px;
    background: linear-gradient(180deg, #6b4a3c 0%, #3e2a24 55%, #1c1a1a 100%);
  }
  .footer-band { position: absolute; left: 0; top: 661px; width: 523px; height: 79px; }
  .contact-block {
    position: absolute; left: 30px; top: 682px;
    font-family: 'Lato', sans-serif; font-weight: 700; color: #fff; font-size: 12.5px;
  }
  .phone-row { display: flex; gap: 10px; align-items: center; height: 20px; }
  .phone { display: flex; align-items: center; gap: 4px; }
  .phone svg { width: 14px; height: 12px; }
  .office-address { margin-top: 4px; }
  .agent-name {
    position: absolute; right: 25px; top: 688px;
    font-family: 'Lato', sans-serif; font-weight: 900; font-size: 22px;
    color: var(--brand-red); text-align: right;
  }
  .agent-brokerage {
    position: absolute; right: 25px; top: 713px;
    font-family: 'Lato', sans-serif; font-weight: 400; font-size: 13px;
    color: var(--muted); text-align: right;
  }
</style>
</head>
<body>
  <main class="flyer">
    <div class="hero-photo" role="img" aria-label="Photo of a large stucco home at dusk with lit arched entry, trees and lawn"></div>

    <div class="headline-panel">
      <div class="headline-city">Lehighton</div>
      <div class="headline-main">OPPORTUNITY</div>
      <div class="headline-tail">is Knocking in 2020</div>
    </div>

    <ul class="market-points">
      <li>Industry is moving in</li>
      <li>Housing Inventory is Critically Low</li>
      <li>Entry Level Homes in High Demand</li>
      <li>Qualified Buyers are searching.</li>
      <li>Now Interest Rates Projected to Rise</li>
    </ul>

    <div class="call-to-action">NOW IS<br>THE TIME<br>TO SELL</div>

    <div class="agent-bio">
      <p>I have been a full time real estate agent<br>serving Carbon and Monroe Counties since 2012.<br>I have been blessed with a successful track record.</p>
      <p>Being in real estate I learn something new to bring to<br>the table for my clients every day. ...</p>
    </div>

    <div class="agent-headshot" role="img" aria-label="Agent headshot portrait"></div>

    <svg class="footer-band" viewBox="0 0 523 79" aria-hidden="true">
      <defs>
        <linearGradient id="footerShade" x1="0" y1="0" x2="1" y2="0">
          <stop offset="0" stop-color="#3b3b3f"/>
          <stop offset="1" stop-color="#5a5a5f"/>
        </linearGradient>
      </defs>
      <path d="M0 0 H235 Q244 0 250 6 L300 66 Q305 72 314 72 H523 V79 H0 Z" fill="url(#footerShade)"/>
    </svg>

    <div class="contact-block">
      <div class="phone-row">
        <span class="phone">
          <svg viewBox="0 0 14 12" aria-hidden="true"><path d="M1 3 Q7 -1 13 3 L12 5 L9.5 4.5 L9 3 Q7 2.5 5 3 L4.5 4.5 L2 5 Z M3 6 H11 L12.5 11 H1.5 Z" fill="#e5333b"/></svg>
          484.927.3160
        </span>
        <span class="phone">
          <svg viewBox="0 0 14 12" aria-hidden="true"><path d="M1 3 Q7 -1 13 3 L12 5 L9.5 4.5 L9 3 Q7 2.5 5 3 L4.5 4.5 L2 5 Z M3 6 H11 L12.5 11 H1.5 Z" fill="#e5333b"/></svg>
          610.718.2295
        </span>
      </div>
      <div class="office-address">2715 Pellow Rd, Whitehall Pa 18094</div>
    </div>

    <div class="agent-name">ODILE BRANKETT</div>
    <div class="agent-brokerage">Hearthway Realty Partners</div>
  </main>
</body>
</html>
```